SaaS Early tech startup business card design

Unique design for experience ecommerce platform company. the business cards will be used by executive members. conformance with color code is required.

```html
<!DOCTYPE html>
<html lang="en">
<head>
<meta charset="utf-8">
<title>Novira — Business Card</title>
<link href="https://fonts.googleapis.com/css2?family=Lato:wght@700;900&family=Arimo:wght@400&display=swap" rel="stylesheet">
<style>
  :root {
    --page: #e2e2e2;
    --card: #212137;
    --teal: #16b39b;
    --teal-deep: #1a97a6;
    --band-top: #0c96a6;
    --band-bottom: #06707c;
    --text-light: #e6e6ea;
    --rule: #4a4a66;
  }
  * { margin: 0; padding: 0; box-sizing: border-box; }
  html, body { width: 1093px; height: 1200px; overflow: hidden; }
  body { background: var(--page); position: relative; font-family: "Arimo", Arial, sans-serif; }

  .card {
    position: absolute;
    left: 264px;
    width: 580px;
    height: 357px;
    background: var(--card);
    overflow: hidden;
  }
  .card--front { top: 226px; }
  .card--back { top: 620px; }

  .card__band {
    position: absolute;
    left: 0; right: 0; bottom: 0;
    height: 12px;
    background: linear-gradient(var(--band-top), var(--band-bottom));
  }

  .wordmark {
    position: absolute;
    font-family: "Lato", Arial, sans-serif;
    font-weight: 900;
    color: var(--teal);
    line-height: 1;
    letter-spacing: 1px;
  }
  .card--front .wordmark { right: 30px; top: 62px; font-size: 82px; }
  .card--back .wordmark { left: 0; right: 0; top: 118px; text-align: center; font-size: 112px; }

  .person { position: absolute; left: 33px; top: 186px; }
  .person__name {
    font-family: "Lato", Arial, sans-serif;
    font-weight: 700;
    font-size: 23px;
    color: var(--teal-deep);
    letter-spacing: -0.3px;
    line-height: 1.1;
  }
  .person__role { font-size: 16px; color: var(--text-light); margin-top: 1px; }

  .divider {
    position: absolute;
    left: 188px; top: 225px;
    width: 362px; height: 1px;
    background: var(--rule);
  }

  .contacts { position: absolute; left: 33px; top: 258px; list-style: none; }
  .contacts li {
    display: flex; align-items: center;
    height: 21px;
    font-size: 16px;
    color: var(--text-light);
  }
  .contacts svg { width: 15px; height: 15px; margin-right: 6px; flex: none; }
  .contacts .accent { color: var(--teal); }

  .address {
    position: absolute;
    right: 40px; top: 279px;
    text-align: right;
    font-size: 16px;
    line-height: 21px;
    color: var(--text-light);
    font-style: normal;
  }
</style>
</head>
<body>

<section class="card card--front" aria-label="Card front">
  <div class="wordmark">novira</div>

  <div class="person">
    <h1 class="person__name">DANIEL REYES</h1>
    <p class="person__role">Managing Director</p>
  </div>
  <div class="divider"></div>

  <ul class="contacts">
    <li>
      <svg viewBox="0 0 16 16" aria-hidden="true"><path d="M4 1.5l2.2 3-1.4 1.6c.8 1.8 2.3 3.3 4.1 4.1l1.6-1.4 3 2.2-1.3 2.5C7.3 13.3 2.7 8.7 1.5 2.8z" fill="none" stroke="#16b39b" stroke-width="1.5" stroke-linejoin="round"/><path d="M10 2a4 4 0 0 1 4 4M10 4.5a1.6 1.6 0 0 1 1.5 1.5" fill="none" stroke="#16b39b" stroke-width="1.3"/></svg>
      044-555 018 273
    </li>
    <li>
      <svg viewBox="0 0 16 16" aria-hidden="true"><rect x="0.5" y="3" width="15" height="10" fill="#16b39b"/><path d="M0.5 3.5L8 9l7.5-5.5" fill="none" stroke="#212137" stroke-width="1.2"/></svg>
      hello@noviramail.com
    </li>
    <li>
      <svg viewBox="0 0 16 16" aria-hidden="true"><g fill="none" stroke="#16b39b" stroke-width="1.2"><circle cx="8" cy="8" r="7"/><ellipse cx="8" cy="8" rx="3" ry="7"/><path d="M1 8h14M2 4.5h12M2 11.5h12M8 1v14"/></g></svg>
      www.<span class="accent">noviraplatform</span>.com
    </li>
  </ul>

  <address class="address">
    318, Harbour Lane, Suite 12<br>
    20417, Eastland
  </address>

  <div class="card__band"></div>
</section>

<section class="card card--back" aria-label="Card back">
  <div class="wordmark">novira</div>
  <div class="card__band"></div>
</section>

</body>
</html>
```